Velvet Hours funky jazz CD Layout design

Cd cover for smooth jazz / funky groove piano based artist. Winning cover designer should be prepared to complete 6 panel CD package layout.

Martin Delvano Velvet Hours

Melodic, organic, soulful, elegant, romantic and fun uptempo instrumental soul / jazz music. Cd design should translate well to 12" sq. flats for promotional use. Looking for a clean, sophisticated, design with artist's name and title prominent.
check out www.delvanotunes.example for musical and graphic samples of what I do. Thanks, martin

Target Market(s)

Smooth Jazz and Instrumental music fans. Wine lovers, the good life.

Industry/Entity Type

Promotional

Font styles to use
Sans Serif

Requirements
Must have
• Elements delivered also as separate files for full package layout and flyer usage.
Nice to have
• UPDATE: See FILES:

My team likes this concept, with the eyes........ and I'd like to get submissions using some of these pics, with alternate, classy TYPE. Current preference is w/ lace fan #....675, but we're open. No Burka look though.

Winner will also be expected to layout 6 panel design. Thanks, Martin

Possible elements: Piano or implied shape or shadow. Sultry woman, possibly close up of enigmatic ( secret) expression.
Has to be compelling design, don't put a piano keyboard just for the sake of it.
Strong Brightmore-like graphic retro / or Red Lantern Discs block style.
Should not have
• No Burka look Flowery, fantasy or hand drawn illustration style.

```html
<!DOCTYPE html>
<html lang="en">
<head>
<meta charset="utf-8">
<title>Martin Delvano – Velvet Hours</title>
<link href="https://fonts.googleapis.com/css2?family=Oswald:wght@500&family=Roboto+Condensed:wght@300&display=swap" rel="stylesheet">
<style>
  :root {
    --stage: #5e5e68;
    --cover: #f4f4f4;
    --ink: #2a2a2e;
    --ink-soft: #1d1d20;
    --wine-1: #5b3b3c;
    --wine-2: #7d3c39;
    --wine-3: #a9423c;
    --wine-4: #c9463e;
    --wine-5: #dc4a40;
    --lace-red: #d8242b;
    --lace-dark: #1b1516;
  }
  html, body {
    margin: 0;
    width: 1200px;
    height: 999px;
    overflow: hidden;
    background: var(--stage);
  }
  .cover {
    position: absolute;
    left: 160px;
    top: 60px;
    width: 880px;
    height: 880px;
    background: var(--cover);
    overflow: hidden;
  }
  .artist-name {
    position: absolute;
    left: 60px;
    right: 60px;
    top: 70px;
    display: flex;
    justify-content: space-between;
    margin: 0;
    font-family: "Oswald", "Arial Narrow", sans-serif;
    font-weight: 500;
    font-size: 70px;
    line-height: 1;
    color: var(--ink);
  }
  .artist-name .gap { width: 14px; }
  .artist-name .tone-1 { color: var(--wine-1); }
  .artist-name .tone-2 { color: var(--wine-2); }
  .artist-name .tone-3 { color: var(--wine-3); }
  .artist-name .tone-4 { color: var(--wine-4); }
  .artist-name .tone-5 { color: var(--wine-5); }
  .name-rule {
    position: absolute;
    left: 0;
    top: 160px;
    width: 700px;
    height: 3px;
    background: linear-gradient(90deg, var(--ink-soft) 0%, var(--ink) 70%, rgba(42,42,46,0) 100%);
  }
  .portrait {
    position: absolute;
    left: 0;
    top: 166px;
    width: 880px;
    height: 522px;
    background:
      linear-gradient(90deg, rgba(244,244,244,0) 55%, var(--cover) 88%),
      linear-gradient(180deg, rgba(27,21,22,0.0) 0%, rgba(27,21,22,0) 45%, rgba(216,36,43,0.85) 60%, rgba(120,20,24,0.9) 100%),
      linear-gradient(100deg, var(--lace-dark) 0%, #3a1a1c 18%, var(--lace-red) 36%, #e86a66 55%, #f3d6d3 72%, var(--cover) 90%);
  }
  .album-title {
    position: absolute;
    right: 66px;
    bottom: 60px;
    margin: 0;
    font-family: "Roboto Condensed", "Arial Narrow", sans-serif;
    font-weight: 300;
    font-size: 78px;
    line-height: 1;
    color: var(--ink-soft);
    text-transform: lowercase;
  }
</style>
</head>
<body>
  <main class="cover">
    <h1 class="artist-name" aria-label="Martin Delvano">
      <span>M</span><span>A</span><span>R</span><span>T</span><span>I</span><span>N</span>
      <span class="gap"></span>
      <span>D</span><span>E</span><span class="tone-1">L</span><span class="tone-2">V</span><span class="tone-3">A</span><span class="tone-4">N</span><span class="tone-5">O</span>
    </h1>
    <div class="name-rule"></div>
    <div class="portrait" role="img" aria-label="Close-up photograph of a woman's eye above a red lace fan, in red, black and white tones"></div>
    <h2 class="album-title">Velvet Hours</h2>
  </main>
</body>
</html>
```